Motor Mate 4x6 Flyer

Need 4 x 6 Flyer with following language:

Willow Crest Motor Mate
Our Motor Mate Will Come to Your Home
Our Motor Mate will Drive Your Car to Nearest Gas Station
Our Motor Mate will Fill-up Your Car with Gas
Our Motor Mate will Immediately Return Your Car
Your Car Covered with $100k of Commercial Insurance
Member Dunmore Chamber of Commerce / Honest Merchant League
www.willowcrestmotormate.example

Place logos of Vortan, Brenn & Dorvane on Left Side of Flyer starting at top left corner, mid left side, left bottom corner.
Place logos of BoltNest, 12-Forty, Tesmira on opposite side right.....
Place Willow Crest Motor Mate Logo on both sides of very top that says Willow Crest Motor Mate

Target Market(s)

Upscale Home Owners

Font styles to use
Sans Serif

Colors
F0912C
F2A743
F7CA91
FBE8D2
FDF5EE

Requirements
Must have
• Flyer Must be Bright Orange

```html
<!DOCTYPE html>
<html lang="en">
<head>
<meta charset="utf-8">
<title>Motor Mate Flyer</title>
<link href="https://fonts.googleapis.com/css2?family=Alegreya+Sans:wght@400;500&family=Josefin+Sans:wght@600;700&display=swap" rel="stylesheet">
<style>
  :root{
    --orange-deep:#c04f0c;
    --orange:#e0711f;
    --orange-bright:#f0912c;
    --amber:#f2a743;
    --peach:#f7ca91;
    --cream:#fbe8d2;
    --paper:#fdf5ee;
    --white:#ffffff;
    --ink:#1a0d05;
    --tick:#e8242a;
  }
  *{margin:0;padding:0;box-sizing:border-box}
  html,body{width:1200px;height:1200px;overflow:hidden;background:var(--white)}
  .flyer{
    position:absolute;left:220px;top:30px;width:760px;height:1140px;overflow:hidden;
    background:linear-gradient(180deg,var(--orange-bright) 0%,var(--orange) 40%,var(--orange-deep) 100%);
  }
  .layer{position:absolute;left:0;top:0}
  .brand-name{
    position:absolute;left:0;width:760px;top:208px;text-align:center;
    font-family:"Josefin Sans",sans-serif;font-weight:700;font-size:54px;color:var(--white);letter-spacing:1px;
  }
  .section-title{
    position:absolute;left:0;width:760px;top:400px;text-align:center;
    font-family:"Josefin Sans",sans-serif;font-weight:600;font-size:29px;letter-spacing:6px;color:var(--paper);
  }
  .service-list{list-style:none;position:absolute;left:84px;top:0;width:640px}
  .service-item{
    position:absolute;left:0;width:640px;display:flex;align-items:flex-start;
    font-family:"Alegreya Sans",sans-serif;font-weight:500;font-size:24px;line-height:32px;color:var(--paper);
  }
  .service-item svg{flex:none;width:32px;height:32px;margin-top:-10px;margin-right:19px}
  .partners{
    position:absolute;left:0;width:760px;top:950px;display:flex;justify-content:space-around;padding:0 40px;
    font-family:"Alegreya Sans",sans-serif;font-weight:500;font-size:26px;color:var(--orange-deep);
  }
  .partner{display:flex;align-items:center;gap:8px}
  .partner i{display:block;width:14px;height:14px;background:var(--orange-deep)}
  .site-url{
    position:absolute;left:0;width:760px;top:1078px;text-align:center;
    font-family:"Josefin Sans",sans-serif;font-weight:600;font-size:28px;letter-spacing:2px;color:var(--white);
  }
</style>
</head>
<body>
<main class="flyer">
  <svg class="layer hero" width="760" height="440" viewBox="0 0 760 440" role="img" aria-label="Photo of a smiling driver in her car giving a thumbs up">
    <defs>
      <linearGradient id="heroTone" x1="0" y1="0" x2="1" y2="1">
        <stop offset="0" stop-color="#f2a743"/>
        <stop offset="0.45" stop-color="#c9671c"/>
        <stop offset="0.8" stop-color="#8a3d0e"/>
        <stop offset="1" stop-color="#f2a743"/>
      </linearGradient>
      <linearGradient id="glow" x1="0" y1="0" x2="0" y2="1">
        <stop offset="0" stop-color="#f7ca91" stop-opacity="0.55"/>
        <stop offset="1" stop-color="#f0912c" stop-opacity="0"/>
      </linearGradient>
    </defs>
    <path d="M0 248 Q380 436 760 240 L760 330 Q380 480 0 330 Z" fill="url(#glow)"/>
    <path d="M0 0 H760 V240 Q380 412 0 248 Z" fill="url(#heroTone)"/>
    <path d="M0 248 Q380 412 760 240" fill="none" stroke="var(--ink)" stroke-width="5"/>
  </svg>

  <div class="brand-name">MOTOR MATE</div>

  <h2 class="section-title">SERVICE DESCRIPTIONS</h2>

  <ul class="service-list">
    <li class="service-item" style="top:476px"><svg viewBox="0 0 32 32"><rect x="1" y="10" width="20" height="20" fill="var(--amber)"/><path d="M5 19 L12 26 L29 4" fill="none" stroke="var(--tick)" stroke-width="5" stroke-linecap="round" stroke-linejoin="round"/></svg><span>Our Motor Mate Will Come to Your Home</span></li>
    <li class="service-item" style="top:529px"><svg viewBox="0 0 32 32"><rect x="1" y="10" width="20" height="20" fill="var(--amber)"/><path d="M5 19 L12 26 L29 4" fill="none" stroke="var(--tick)" stroke-width="5" stroke-linecap="round" stroke-linejoin="round"/></svg><span>Our Motor Mate will Drive Your Car to the Nearest Gas Station</span></li>
    <li class="service-item" style="top:613px"><svg viewBox="0 0 32 32"><rect x="1" y="10" width="20" height="20" fill="var(--amber)"/><path d="M5 19 L12 26 L29 4" fill="none" stroke="var(--tick)" stroke-width="5" stroke-linecap="round" stroke-linejoin="round"/></svg><span>Our Motor Mate will Fill-up Your Car with Gas</span></li>
    <li class="service-item" style="top:665px"><svg viewBox="0 0 32 32"><rect x="1" y="10" width="20" height="20" fill="var(--amber)"/><path d="M5 19 L12 26 L29 4" fill="none" stroke="var(--tick)" stroke-width="5" stroke-linecap="round" stroke-linejoin="round"/></svg><span>Our Motor Mate will Immediately Return Your Car</span></li>
    <li class="service-item" style="top:718px"><svg viewBox="0 0 32 32"><rect x="1" y="10" width="20" height="20" fill="var(--amber)"/><path d="M5 19 L12 26 L29 4" fill="none" stroke="var(--tick)" stroke-width="5" stroke-linecap="round" stroke-linejoin="round"/></svg><span>Your Car Covered with $100k of Commercial Insurance</span></li>
    <li class="service-item" style="top:771px"><svg viewBox="0 0 32 32"><rect x="1" y="10" width="20" height="20" fill="var(--amber)"/><path d="M5 19 L12 26 L29 4" fill="none" stroke="var(--tick)" stroke-width="5" stroke-linecap="round" stroke-linejoin="round"/></svg><span>Member Dunmore Chamber of Commerce / Honest Merchant League</span></li>
  </ul>

  <svg class="layer torn-band" width="760" height="1140" viewBox="0 0 760 1140" aria-hidden="true">
    <path fill="var(--white)" d="M0 870 L18 865 L34 872 L52 860 L70 864 L88 856 L104 862 L122 858 L140 870 L158 866 L176 874 L196 868 L214 880 L232 876 L250 884 L270 878 L290 888 L308 882 L326 890 L344 884 L362 878 L382 882 L400 872 L420 880 L440 870 L458 876 L476 882 L494 878 L512 888 L530 884 L548 880 L566 872 L584 876 L602 866 L622 870 L640 860 L656 856 L674 866 L692 862 L710 868 L728 872 L746 866 L760 870
      L760 1052 L742 1056 L724 1050 L706 1058 L688 1054 L670 1062 L650 1058 L632 1064 L614 1060 L596 1066 L576 1062 L556 1068 L538 1064 L518 1070 L500 1066 L482 1060 L462 1064 L444 1058 L426 1066 L406 1060 L388 1052 L370 1056 L350 1050 L330 1058 L312 1054 L294 1060 L274 1056 L256 1062 L236 1058 L216 1064 L198 1058 L180 1052 L160 1056 L142 1050 L122 1054 L104 1048 L86 1052 L66 1046 L48 1050 L30 1044 L14 1048 L0 1046 Z"/>
  </svg>

  <div class="partners">
    <span class="partner">Brenn</span>
    <span class="partner">Dorvane</span>
    <span class="partner">Vortan</span>
    <span class="partner">BoltNest</span>
    <span class="partner">12-Forty</span>
    <span class="partner">Tesmira</span>
  </div>

  <p class="site-url">www.willowcrestmotormate.example</p>
</main>
</body>
</html>
```